Quick Straightforward Billboard Redesign

- Design billboard sized for 10 foot' x 36' foot width live area size and please include bleeds 6" around all sides
- Exact blue color match is imperative in headline, logo, phone number bubble or wherever used. C-83 / M-45 / Y-1 / K-0-
- What I hope to illustrate is that our company offers the best porch screening in the area area, in regards to quality, expertise, durability, storms proof, but we do not build screen porches.
- Current board is attached below from previous designer, and as you can see sizing was off, white space on edges make it appear to be sized incorrectly.
- I also attached my own little mock up idea well well if it helps, favorite image, logo, headline, etc and ideas perhaps on expanding or making this better?

Thanks so much!

Target Market(s)

Drivers and passengers, Southeastern NC, are of immense new construction and high end homes.

Industry/Entity Type

Construction

Colors
0054AA
0677BA
7BADD7
CADEEF
E8F1F8

Requirements
Must have
• Blue color matching
Nice to have
• Design spins or other thoughts on my little mock up

```html
<!DOCTYPE html>
<html lang="en">
<head>
<meta charset="UTF-8">
<title>Baywind Mesh Co. Billboard</title>
<link href="https://fonts.googleapis.com/css2?family=Anton&family=Oswald:wght@400;600&display=swap" rel="stylesheet">
<style>
  :root {
    --brand-blue: #0a6db8;
    --phone-blue: #0658a8;
    --coast-green: #00b45e;
    --white: #ffffff;
    --mark-tone: #f4efe1;
    --stage: #3a3a3a;
  }
  * { box-sizing: border-box; margin: 0; padding: 0; }
  html, body { width: 1145px; height: 1200px; overflow: hidden; background: var(--stage); }
  .canvas { position: relative; width: 1145px; height: 1200px; }
  .billboard {
    position: absolute; left: 30px; top: 437px;
    width: 1085px; height: 325px;
    background: var(--brand-blue);
    box-shadow: 0 10px 28px rgba(0,0,0,.55);
    overflow: hidden;
  }
  .porch-photo {
    position: absolute; left: 0; top: 0; width: 373px; height: 325px;
    background: linear-gradient(180deg, #ecebe6 0%, #dcdcd6 18%, #8fbfe6 30%, #7aa46a 45%, #6f6a5c 62%, #8a7f70 75%, #d8d0c2 100%);
  }
  .headline {
    position: absolute; left: 404px; top: 0; height: 112px; right: 20px;
    display: flex; align-items: center;
    font-family: "Anton", sans-serif; font-size: 84px; line-height: 1;
    color: var(--white); letter-spacing: -0.5px; white-space: nowrap;
  }
  .tagline-band {
    position: absolute; left: 361px; right: 0; top: 112px; height: 82px;
    background: var(--coast-green);
    display: flex; align-items: center; padding-left: 43px;
    font-family: "Anton", sans-serif; font-size: 76px; line-height: 1;
    color: var(--white); letter-spacing: 1px; text-transform: uppercase; white-space: nowrap;
  }
  .company {
    position: absolute; left: 404px; top: 214px; height: 83px;
    display: flex; align-items: center; gap: 12px;
  }
  .company-mark { width: 18px; height: 18px; border-radius: 50%; background: var(--white); flex: none; }
  .company-name {
    font-family: "Oswald", sans-serif; font-weight: 600; font-size: 31px;
    line-height: 1; color: var(--white); white-space: nowrap;
  }
  .phone-pill {
    position: absolute; left: 673px; right: 0; top: 214px; height: 83px;
    background: var(--white); border-radius: 20px 0 0 20px;
    box-shadow: 0 8px 14px rgba(0,0,0,.25);
    display: flex; align-items: center; padding-left: 16px; gap: 14px;
  }
  .phone-icon { width: 42px; height: 42px; flex: none; }
  .phone-number {
    font-family: "Oswald", sans-serif; font-weight: 600; font-size: 56px;
    line-height: 1; color: var(--phone-blue); letter-spacing: -0.5px; white-space: nowrap;
  }
</style>
</head>
<body>
<div class="canvas">
  <section class="billboard">
    <div class="porch-photo" role="img" aria-label="Photo of a screened covered porch with wicker lounge chairs, ceiling fan and a view of a lake"></div>
    <h1 class="headline">Screen your Porch.</h1>
    <div class="tagline-band">Built for the Coast.</div>
    <div class="company">
      <span class="company-mark"></span>
      <p class="company-name">Baywind Mesh Co.</p>
    </div>
    <div class="phone-pill">
      <svg class="phone-icon" viewBox="0 0 42 42" aria-hidden="true">
        <circle cx="21" cy="21" r="20" fill="#00b45e" stroke="#e4f4ea" stroke-width="2"/>
        <path d="M14.5 11.5c1-.6 2-.3 2.6.6l2 3.2c.5.8.3 1.8-.4 2.4l-1.3 1c.9 2 2.6 3.8 4.6 4.8l1-1.3c.6-.7 1.6-.9 2.4-.4l3.2 2c.9.6 1.2 1.7.6 2.6l-1 1.6c-.8 1.2-2.3 1.7-3.7 1.2-5.6-2-10-6.4-12-12-.5-1.4 0-2.9 1.2-3.7z" fill="#fff"/>
        <path d="M23 12.5a6.5 6.5 0 0 1 6.5 6.5M23 15.8a3.2 3.2 0 0 1 3.2 3.2" fill="none" stroke="#fff" stroke-width="1.6" stroke-linecap="round"/>
      </svg>
      <span class="phone-number">910.555.0142</span>
    </div>
  </section>
</div>
</body>
</html>
```